high end kitchens , needing new logo and business card design .

im looking a very simple looking design but classy that will stand out , i would like the design to be in the colours black , silver , gold and grey , although all colours dont need to be used in design , back of card to have name on it colin farrow , address and phone number and website address , maybe fb logo . adrress is 27 orchard row , newtownards , bt19 4qd , 07812459067 , front of the card im open to design , back of card very simple i will want it matt black with silver writing , writing doesnt need to be that big

Target Market(s)

people with kitchen projects .

Industry/Entity Type

Interior Design

Contact Information for Business Card

front of business card lg on it with maybe lumen galley under it wrote smaller , maybe the card to be mate black with the writing in a gloss black or silver

Logo Text

lg . lumen galley

Font styles to use
Sans Serif
Script

Colors
1b1b1b
919191
f6f6f6
848484
ffc214
ec1f27

Requirements
Must have
• clean and simple , not too fussy ,
Nice to have
• n/a
Should not have
• n/a

```html
<!DOCTYPE html>
<html lang="en">
<head>
<meta charset="utf-8">
<title>Lumen Galley – Business Card</title>
<link href="https://fonts.googleapis.com/css2?family=Gelasio:wght@400&family=Questrial&display=swap" rel="stylesheet">
<style>
  :root {
    --backdrop: #e6e3df;
    --card-black: #000000;
    --silver: #ececec;
    --silver-soft: #dcdcdc;
  }
  html, body {
    margin: 0;
    width: 1200px;
    height: 1186px;
    overflow: hidden;
    background: var(--backdrop);
  }
  .canvas {
    position: relative;
    width: 1200px;
    height: 1186px;
  }
  .card {
    position: absolute;
    left: 105px;
    width: 690px;
    height: 384px;
    background: var(--card-black);
    color: var(--silver);
    box-shadow: 0 6px 18px rgba(0,0,0,0.18);
  }
  .card--contact { top: 272px; }
  .card--brand { top: 714px; }

  .holder-name {
    position: absolute;
    left: 0;
    right: 0;
    top: 62px;
    margin: 0;
    text-align: center;
    font-family: "Gelasio", Georgia, serif;
    font-weight: 400;
    font-size: 62px;
    letter-spacing: 0.5px;
    line-height: 1;
    color: var(--silver);
  }
  .name-rule {
    position: absolute;
    left: 190px;
    top: 146px;
    width: 316px;
    height: 2px;
    background: var(--silver);
  }
  .web-icon {
    position: absolute;
    left: 172px;
    top: 207px;
    width: 72px;
    height: 72px;
  }
  .web-address {
    position: absolute;
    left: 108px;
    width: 200px;
    top: 294px;
    text-align: center;
    font-family: "Questrial", "Century Gothic", sans-serif;
    font-size: 18px;
    letter-spacing: 0.6px;
    color: var(--silver);
  }
  .column-divider {
    position: absolute;
    left: 345px;
    top: 196px;
    width: 2px;
    height: 140px;
    background: var(--silver);
  }
  .contact-list {
    position: absolute;
    left: 374px;
    top: 210px;
    margin: 0;
    padding: 0;
    list-style: none;
  }
  .contact-item {
    display: flex;
    align-items: center;
    height: 32px;
    margin-bottom: 7px;
    font-family: "Questrial", "Century Gothic", sans-serif;
    font-size: 20px;
    letter-spacing: 0.6px;
    color: var(--silver);
  }
  .contact-item svg {
    width: 32px;
    height: 32px;
    margin-right: 20px;
    flex: none;
  }
  .contact-item--phone { font-size: 17px; }

  .brand-block {
    position: absolute;
    left: 130px;
    top: 143px;
    display: flex;
    align-items: center;
  }
  .brand-square {
    width: 100px;
    height: 100px;
    background: var(--silver);
    margin-right: 58px;
  }
  .brand-name {
    margin: 0;
    font-family: "Gelasio", Georgia, serif;
    font-weight: 400;
    font-size: 56px;
    line-height: 58px;
    letter-spacing: 0.5px;
    color: var(--silver);
    text-transform: uppercase;
  }
</style>
</head>
<body>
<div class="canvas">

  <section class="card card--contact" aria-label="Business card back">
    <h1 class="holder-name">Colin Farrow</h1>
    <div class="name-rule"></div>

    <svg class="web-icon" viewBox="0 0 72 72" aria-hidden="true">
      <circle cx="36" cy="36" r="36" fill="var(--silver)"/>
      <g fill="none" stroke="#000" stroke-width="3">
        <circle cx="36" cy="36" r="24"/>
        <ellipse cx="36" cy="36" rx="11" ry="24"/>
        <ellipse cx="36" cy="36" rx="24" ry="10"/>
      </g>
    </svg>
    <div class="web-address">Yourwebsite.com</div>

    <div class="column-divider"></div>

    <ul class="contact-list">
      <li class="contact-item">
        <svg viewBox="0 0 32 32" aria-hidden="true"><circle cx="16" cy="16" r="16" fill="var(--silver)"/></svg>
        <span>YourSocial</span>
      </li>
      <li class="contact-item contact-item--phone">
        <svg viewBox="0 0 32 32" aria-hidden="true">
          <circle cx="16" cy="16" r="16" fill="var(--silver)"/>
          <path d="M11 8 l4 4 -2 3 c1 2 3 4 5 5 l3 -2 4 4 -3 3 c-6 0 -14 -8 -14 -14 z" fill="#000"/>
        </svg>
        <span>00 0000 0000</span>
      </li>
      <li class="contact-item">
        <svg viewBox="0 0 32 32" aria-hidden="true">
          <circle cx="16" cy="16" r="16" fill="var(--silver)"/>
          <path d="M6 16 L16 7 L26 16 L23 16 L23 24 L18 24 L18 19 L14 19 L14 24 L9 24 L9 16 Z" fill="#000"/>
        </svg>
        <span>Your Address</span>
      </li>
    </ul>
  </section>

  <section class="card card--brand" aria-label="Business card front">
    <div class="brand-block">
      <div class="brand-square"></div>
      <p class="brand-name">Lumen<br>Galley</p>
    </div>
  </section>

</div>
</body>
</html>
```